Animal Adoption Page

We are working on re-designing an animal adoption page for one of our clients, and are failing to come up with a modern, cutting edge design that not only looks great, but converts well also. We would like to reach out to the pixelhive community to see some innovative design work that will help us to reach our goal. Unfortunately we can't release details of our client, so the design will need to be based on some generalisations and assumptions.
Firstly, here are some competitor pages to give you an idea of the typical animal adoption process:
- https://help.tarnwick.org.uk/
- http://www.brellowpaws.org.uk/microsites/sponsor-a-puppy
- http://www.quenby.org/adopt
- http://www.globalcritterhaven.org/adopt-an-animal
- http://www.morrowtrust.org/adopt
- http://www.pellington.org.uk/adopt/default.asp
- https://give.wildroam.org.uk/adopt
- http://www.kvt.org/shop/animal-adoptions/category.html
- http://www.hallowmerepark.org/support-us/adoptions
Secondly, here are some details that you should assume about the client:
1. Our client is heavily involved in animal conservation and have a number of animal parks/zoos in the UK
2. They have about 30 animals available for adoption, spread across 6 or 7 species (such as big cats, gorillas, elephants, etc.)
3. Each animal that you can adopt has a name, a biography, facts and personal info (date of birth, keeper, etc.)
4. There are several adoption packages to choose from:
"junior" which is aimed at children and comes with a free cuddly toy
"standard" which is aimed at everyone and has 4 different pricing levels. Each level has slightly different benefits, but usually contain an annual pass to one of the organisations animal parks/zoos. For the purposes of the design, you can choose the names of each pricing level (or if you'd prefer call them level 1, level 2, level 3 and level 4)
"virtual" is aimed at people who do not want the physical goods that come with the other adoptions packages, and just want the good feeling of helping an animal
The typical purchaser of an adoption has the following properties:
1. Most people who purchase adoptions are aged 20-45
2. Adoptions are mostly purchased BY females
3. Most adoptions are purchased FOR women
4. The majority of adoptions are purchased as gifts for other people (about 75%)
5. Gifters (people who purchase gifts for others) are the primary market we're trying to reach with the page, but other types of adopters do exist (animal lovers, people who enjoy conservation, people who want more than just a ticket to one of the parks/zoos) and these should be catered for also
What MUST the design incorporate?
- The design must show a complete design for the adoption purchase process. This includes the first page they see when they click on the "adopt" navigation link, the animal selection process, the adoption package selection process, how animal details are displayed during the process and the checkout process.
- The process must be clear and concise and very user friendly
- The design must use high quality imagery throughout. Only real photos of animals are allowed (no drawings or cartoons) but animal silhouettes are acceptable. A selection of high quality images have been provided to help guide you but you are in no way limited to using these
What SHOULD the design incorporate
- We'd like the final deign to be based on a single page website concept. You can get lots of inspiration from here - http://www.plaudify.com/websites/parallax/. The closest design from the current competitors is the one for quenby.org
- The process must take into consideration conversion rates and try to be optimised
- You can design the page to use any sort of fancy javascript or jquery effects and animation. there is no need to code these, just describe how the effects will work in a document (with images where applicable)
- The design will ideally be image led, with nice large background images
What DOES NOT need to be included
- A logo design - just use a placeholder
- Any HTML or Javascript - we just need a high quality layered photoshop file from the winner
- Copy - Feel free to use lorem ipsum text where copy should go, but please describe what the copy is intended to be about either in the design or in a separate document (e.g. box 1 should contain a description of the animal species)
Colours/Brand
The new website that is being designed for the client uses two fonts throughout. For headings they use Helvetica Neue 97 Black Condensed, and for body text they use Futura PT. If you do not have these fonts, you can use equivalents but try to keep them as close to the originals as possible.
Throughout the site pages, the fonts tend to be white, and are against dark earthy coloured backgrounds. The primary palette of the site is earthy colours such as browns, greens, oranges and greys. Black is also featured heavily as a background colour.
The site comprises of lots of large background images which take up most of the users browser viewport. By default we'd like you to continue this on the adoption pages, but we're open to suggestions.
When large background images are used, and text needs to be placed over the top, the site uses semi-opaque rectangles (either 28%, 64% or 84%) as a background to the text.
Overall the site uses largely flat design principles, and when there are buttons for the user to click on, they are placed on flat rectangles (not rounded) with solid background colours.
Last comments
Overall, we are looking for something unique and cutting edge. Over the years, our client has tried using most of the approaches currently followed by our competitors with varying levels of success, but ultimately we feel there is a lot that can be done to improve the process, and are looking for a forward thinking design, that use as many cutting edge technology and design concepts as needed. We are not afraid to push the boundaries of technology and design - so feel free to think a little radically.
The winning design will be the one that provides us with the most inspiration for our final design. There are secondary prizes for any other designs that provide us with significant inspiration for our final design.
UPDATE 1: A number of designers have asked us whether the designs need to include a mobile interface. We can confirm that the smallest screensize we expect to view this page is a portrait tablet, with a screen resolution of 720px x 1024px. Anything smaller than this will be served by a separate mobile site that we will design.
UPDATE 2: From the designs we have received so far they have all had a key element missing, and we have realised this wasn't explained well enough in the original brief. We would like to see a thank you page or panel that will be displayed to the user after they have made an adoption. The elements that should be visible on this page are: 1) a thank you message, 2) the ability to share the adoption on their social networks, 3) an encouragement to share their adoption certificate on their chirpnest account (probably by installing a custom chirpnest app) and 4) to download a mobile app that they get free as part of their adoption
Reason: Due to requests from a few different designers we have decided to extend the deadline of this project by 5 days. This will enable all designers who have taken part to revise their designs in accordance with our feedback and provide an opportunity for new designers to submit design ideas.
- Helvetica Neue 97 black Condensed (for headers), Futura PT Body (for body)

```html
<!DOCTYPE html>
<html lang="en">
<head>
<meta charset="utf-8">
<title>UK Animal Adoption – Adoption process</title>
<link rel="stylesheet" href="https://fonts.googleapis.com/css2?family=Arimo:ital,wght@0,400;0,700;1,400;1,700&family=Great+Vibes&display=swap">
<style>
:root{
  --lavender:#bbb3fb;
  --panel-grey:#7f7f7f;
  --dark:#3a3a3a;
  --green:#77bd5c;
  --nav-green:#b9ff7a;
  --bio-label:#c9ff9a;
  --ink-blue:#2a2af0;
  --script-blue:#5a52e6;
  --card-bg:#ebe9ee;
  --price-oval:#b8b0f2;
  --orange:#f08a1a;
  --yellow:#ffe600;
  --white:#ffffff;
  --black:#000000;
}
*{box-sizing:border-box;margin:0;padding:0}
html,body{width:1200px;height:1000px;overflow:hidden;background:var(--white)}
body{position:relative;font-family:"Arimo",Arial,sans-serif}
.abs{position:absolute}

/* header */
.site-header{left:400px;top:10px;width:400px;height:32px;
  background:linear-gradient(to bottom,#e53a22 0 3px,#f28a2a 3px 6px,var(--dark) 6px 26px,var(--green) 26px 32px)}
.logo{left:410px;top:6px;width:60px;height:42px;background:#4a4a4a;border:1px solid #222;
  color:var(--white);font-size:13px;letter-spacing:2px;display:flex;align-items:center;justify-content:center;box-shadow:2px 2px 2px rgba(0,0,0,.5)}
.site-name{left:476px;top:22px;color:var(--white);font-size:7.5px;font-weight:700}
.nav{left:560px;top:24px;width:240px;display:flex;justify-content:space-around;list-style:none}
.nav li{color:var(--nav-green);font-size:5.5px;font-weight:700}
.page-title{left:401px;top:65px;color:var(--ink-blue);font-size:13px;letter-spacing:2px}

/* shared */
.band-grey{background:var(--panel-grey)}
.band-lav{background:var(--lavender)}
.script{font-family:"Great Vibes",cursive;color:var(--script-blue);font-size:34px;line-height:1}
.shadow{box-shadow:0 4px 5px rgba(0,0,0,.45)}

/* animal */
.animal-name{left:414px;top:132px;width:184px;text-align:center;font-weight:700;font-size:16px;letter-spacing:3px;color:var(--white);
  text-shadow:-1px -1px 0 #000,1px -1px 0 #000,-1px 1px 0 #000,1px 1px 0 #000}
.animal-photo{left:414px;top:154px;width:182px;height:186px;border:4px solid var(--black);border-radius:12px;
  background:linear-gradient(135deg,#3c5a2e,#c89a5a 45%,#e0cfae 60%,#2e3d22)}
.bio{left:622px;top:97px;width:169px;height:242px;background:var(--green);border:2px solid #444}
.bio-head{position:absolute;left:0;right:0;top:12px;height:18px;background:linear-gradient(to bottom,#fff,#c7c0ff);
  font-family:"Great Vibes",cursive;color:var(--bio-label);font-size:15px;text-align:center;text-shadow:0 0 1px #3a7a20}
.bio-row{position:absolute;left:0;width:200px;display:flex;font-size:6.5px;font-weight:700}
.bio-row dt{width:69px;text-align:right;color:var(--bio-label);padding-right:3px}
.bio-row dd{color:var(--white)}
.bio-sub{position:absolute;left:21px;color:var(--bio-label);font-size:6.5px;font-weight:700}
.bio-text{position:absolute;left:21px;width:140px;color:var(--white);font-size:6.3px;font-weight:700;line-height:1.25}

/* packages */
.pkg-label{top:429px;width:86px;text-align:center;color:var(--white);font-size:12px}
.card{top:443px;width:87px;height:150px;background:var(--card-bg);border:4px solid var(--black);border-radius:6px;text-align:center;overflow:hidden}
.card .aim{margin-top:5px;color:var(--ink-blue);font-size:8px;font-style:italic}
.card .aim.big{font-size:11px}
.price{margin:8px auto 0;width:66px;height:22px;border-radius:50%;background:var(--price-oval);
  font-size:11px;font-style:italic;font-weight:700;color:var(--yellow);line-height:22px;
  text-shadow:-1px -1px 0 #000,1px -1px 0 #000,-1px 1px 0 #000,1px 1px 0 #000}
.price-select{display:inline-block;margin-top:5px;background:#6f6a90;color:var(--yellow);font-size:6px;font-weight:700;padding:2px 4px;border-radius:4px}
.perk{margin-top:6px;color:var(--orange);font-size:11.5px;font-style:italic;line-height:1.1}
.perk .num{color:var(--yellow)}
.toy{margin-top:6px;font-size:10px;font-style:italic;line-height:1;color:#d6002a}
.toy span:first-child{color:var(--yellow)}
.cond{text-align:left;margin:6px 0 0 6px;color:var(--ink-blue);font-size:8px;font-style:italic}
.cond-text{text-align:justify;margin:2px 5px 0;font-size:4px;line-height:1.35;color:#222}
.check{top:596px;width:17px;height:17px;background:var(--white);border:2px solid var(--black);border-radius:2px}

/* form */
.form-panel{left:397px;top:653px;width:400px;height:111px;background:var(--lavender)}
.field-label{position:absolute;color:var(--white);font-size:6.5px;font-style:italic;font-weight:700}
.field{position:absolute;height:9px;background:var(--white)}
.basket{position:absolute;left:304px;top:88px;width:60px;height:10px;border-radius:5px;background:#6a6a6a;color:var(--white);
  font-size:6.5px;font-style:italic;font-weight:700;text-align:center;line-height:10px}

/* more animals */
.more{left:396px;top:795px;width:403px;height:150px;background:var(--green)}
.silhouette-strip{position:absolute;left:1px;top:2px;width:401px;height:14px;background:var(--dark)}
.silhouette-strip div{position:absolute;left:26px;top:3px;width:334px;height:8px;background:linear-gradient(to right,#9a9a9a,#d8d8d8,#9a9a9a)}
.more-bar{position:absolute;left:1px;top:26px;width:401px;height:13px;background:var(--dark);color:var(--white);
  font-size:11px;font-style:italic;text-align:center;line-height:13px}
.more-bar svg{position:absolute;top:2px}
.ph{position:absolute}
</style>
</head>
<body>

<header>
  <div class="abs site-header"></div>
  <div class="abs logo">LOGO</div>
  <div class="abs site-name">UK&nbsp; Animal&nbsp; Adoption</div>
  <ul class="abs nav">
    <li>HOME</li><li>ANIMALS</li><li>ADOPTION</li><li>ABOUT US</li><li>CONTACT</li>
  </ul>
</header>

<h1 class="abs page-title" style="font-weight:400">Adoption process</h1>

<!-- chosen animal -->
<section>
  <div class="abs band-grey" style="left:392px;top:113px;width:410px;height:212px"></div>
  <div class="abs band-lav shadow" style="left:396px;top:86px;width:401px;height:36px"></div>
  <div class="abs band-lav" style="left:396px;top:315px;width:401px;height:35px"></div>
  <h2 class="abs script" style="left:440px;top:88px;font-weight:400">You choose:</h2>
  <div class="abs animal-name">THOR</div>
  <div class="abs animal-photo" role="img" aria-label="Photo of Thor the tiger"></div>

  <dl class="abs bio">
    <div class="bio-head">Biography</div>
    <div class="bio-row" style="top:34px"><dt>Date of birth:</dt><dd>January, 20 2003</dd></div>
    <div class="bio-row" style="top:49px"><dt>Keeper:</dt><dd>Tanzania Zoo</dd></div>
    <div class="bio-row" style="top:64px"><dt>Facts:</dt><dd style="font-size:5px">200 Pounds, Blue eyes</dd></div>
    <div class="bio-row" style="top:79px"><dt>Personal info:</dt><dd>Blue Eyes, Born in Tanzania.</dd></div>
    <div class="bio-row" style="top:94px"><dt>Healt:</dt><dd>Good health and strong</dd></div>
    <div class="bio-row" style="top:109px"><dt>Vaccination:</dt><dd>Update.</dd></div>
    <div class="bio-sub" style="top:126px">Description</div>
    <p class="bio-text" style="top:136px">Sit amet, consectetur adipisicing elit, sed do eiusmod tempor incididunt ut labore et dolore magna aliqua. Ut enim ad minim veniam, quis nostrud exercitation ullamco laboris nisi ut aliquip ex ea commodo consequat.</p>
    <div class="bio-sub" style="top:195px">About the actial owner</div>
    <p class="bio-text" style="top:203px">Lorem ipsum dolor sit amet, consectetur adipisicing elit, sed do eiusmod tempor incididunt ut labore et dolore magna aliqua. Ut enim ad minim</p>
  </dl>
</section>

<!-- packages -->
<section>
  <div class="abs band-grey" style="left:392px;top:397px;width:410px;height:211px"></div>
  <div class="abs band-lav shadow" style="left:397px;top:381px;width:401px;height:37px"></div>
  <div class="abs band-lav" style="left:397px;top:580px;width:401px;height:37px"></div>
  <h2 class="abs script" style="left:408px;top:381px;font-weight:400">Select You Package:</h2>

  <div class="abs pkg-label" style="left:403px">Junior</div>
  <div class="abs pkg-label" style="left:503px">Standard</div>
  <div class="abs pkg-label" style="left:603px">Virtual</div>
  <div class="abs pkg-label" style="left:703px">Gifter</div>

  <article class="abs card" style="left:404px">
    <p class="aim big">for children</p>
    <div class="price">Price: 5£</div>
    <p class="toy"><span>Gift</span><br><span style="color:#d6002a">a</span><br>Cuddly<br>Toy</p>
    <p class="cond" style="margin-top:9px">Conditions:</p>
    <p class="cond-text">Lorem ipsum dolor sit amet, consectetur adipiscing elit, sed do eiusmod tempor incididunt ut labore.</p>
  </article>
  <article class="abs card" style="left:504px">
    <p class="aim">Aimed at everyone</p>
    <div class="price" style="background:var(--price-oval);text-shadow:none"><span class="price-select">Select a price ▾</span></div>
    <p class="perk">Annual pass<br><span class="num">to 3</span><br>Park/Zoo</p>
    <p class="cond">Conditions:</p>
    <p class="cond-text">Lorem ipsum dolor sit amet, consectetur adipiscing elit, sed do eiusmod tempor incididunt ut labore.</p>
  </article>
  <article class="abs card" style="left:604px">
    <p class="aim">Just help an animal</p>
    <div class="price">Price: 15£</div>
    <p class="perk">Annual pass<br><span class="num">to 3</span><br>Park/Zoo</p>
    <p class="cond">Conditions:</p>
    <p class="cond-text">Lorem ipsum dolor sit amet, consectetur adipiscing elit, sed do eiusmod tempor incididunt ut labore.</p>
  </article>
  <article class="abs card" style="left:704px">
    <p class="aim big">Gift for other</p>
    <div class="price">Price: 15£</div>
    <p class="perk">Annual pass<br><span class="num">to 3</span><br>Park/Zoo</p>
    <p class="cond">Conditions:</p>
    <p class="cond-text">Lorem ipsum dolor sit amet, consectetur adipiscing elit, sed do eiusmod tempor incididunt ut labore.</p>
  </article>

  <div class="abs check" style="left:435px"></div>
  <div class="abs check" style="left:539px"></div>
  <div class="abs check" style="left:640px"></div>
  <div class="abs check" style="left:740px"></div>
</section>

<!-- checkout -->
<div class="abs band-lav" style="left:582px;top:617px;width:29px;height:36px"></div>
<form class="abs form-panel">
  <span class="field-label" style="left:59px;top:24px">Firstname</span>
  <span class="field" style="left:101px;top:24px;width:103px"></span>
  <span class="field-label" style="left:214px;top:24px">Surname</span>
  <span class="field" style="left:249px;top:24px;width:103px"></span>
  <span class="field-label" style="left:59px;top:46px">Email</span>
  <span class="field" style="left:102px;top:46px;width:206px"></span>
  <span class="field-label" style="left:59px;top:65px">Address</span>
  <span class="field" style="left:102px;top:66px;width:206px"></span>
  <span class="field-label" style="left:59px;top:83px">Postcode</span>
  <span class="field" style="left:102px;top:83px;width:49px"></span>
  <span class="basket">Add to basket</span>
</form>

<!-- more animals -->
<section class="abs more">
  <div class="silhouette-strip"><div role="img" aria-label="Row of animal silhouettes"></div></div>
  <div class="more-bar">
    <svg style="left:11px" width="8" height="9" viewBox="0 0 8 9"><path d="M7 0.5 1 4.5 7 8.5" fill="none" stroke="#fff" stroke-width="1.3"/></svg>
    More animals to adopt
    <svg style="right:11px" width="8" height="9" viewBox="0 0 8 9"><path d="M1 0.5 7 4.5 1 8.5" fill="none" stroke="#fff" stroke-width="1.3"/></svg>
  </div>
  <div class="ph" role="img" aria-label="Photo of a pack of wolves" style="left:0;top:52px;width:104px;height:78px;background:linear-gradient(135deg,#8a8078,#cfc6bb,#6e655c);border-radius:30% 40% 20% 20%"></div>
  <div class="ph" role="img" aria-label="Photo of a resting lion" style="left:136px;top:62px;width:120px;height:76px;background:linear-gradient(135deg,#b07a30,#e0b060,#8a5a20);border-radius:40% 40% 10% 10%"></div>
  <div class="ph" role="img" aria-label="Photo of an oryx" style="left:304px;top:44px;width:99px;height:104px;background:linear-gradient(135deg,#6a6a6a,#d8d4cc,#8a8580);border-radius:30% 0 0 20%"></div>
</section>

</body>
</html>
```